Business Card Trio Design

We need a set of business cards that all match but are not identical. We need one generic for the business and one for each of the two owners. We would like the cards to be similar to each other, but not identical. We have a logo and the colors of the logo are painstakingly chosen so if blue or green is used, we prefer our specific blue and green. Our logo pops better on a black background as well. We are open to double-sided, but it is not the top choice. We would love some either gold or silver accents that are in a foiled appearance. We sell uniforms (scrubs, culinary, EMT, police, fire, business, all types except kids and sports), shoes, equipment, and accessories. We also have facebook, pinterest, instagram, and twitter that we would like to have them follow and we offer splitwell in the store we would like the card to also advertise.

```html
<!DOCTYPE html>
<html lang="en">
<head>
<meta charset="utf-8">
<title>Business Card Options</title>
<link rel="stylesheet" href="https://fonts.googleapis.com/css2?family=Figtree:wght@400;500;600;700&display=swap">
<style>
  :root {
    --page-bg: #03101d;
    --card-bg: #0c1522;
    --brand-blue: #7c9cc2;
    --brand-green: #15966f;
    --title-white: #f2f4f7;
  }
  * { margin: 0; padding: 0; box-sizing: border-box; }
  html, body { width: 1200px; height: 600px; overflow: hidden; background: var(--page-bg); }
  body { position: relative; font-family: "Figtree", sans-serif; }

  .sheet-title {
    position: absolute; top: 48px; left: 0; width: 1200px; text-align: center;
    color: var(--title-white); font-size: 19px; font-weight: 500; letter-spacing: 5.6px;
  }

  .card {
    position: absolute; width: 321px; height: 184px; border-radius: 18px;
    background: var(--card-bg);
    box-shadow: 0 6px 18px rgba(0,0,0,0.45);
  }
  .card--a { left: 36px; }
  .card--b { left: 433px; }
  .card--c { left: 837px; }
  .row-front { top: 110px; }
  .row-back { top: 349px; }

  .brand { position: absolute; display: flex; align-items: center; }
  .brand--stacked { flex-direction: column; gap: 8px; }
  .brand-dot { border-radius: 50%; background: var(--brand-blue); flex: none; }
  .brand-name {
    color: var(--brand-green); font-weight: 600; line-height: 1;
    text-transform: uppercase; text-align: center;
  }
  .brand-name span { display: block; }

  .stacked-lg .brand-dot { width: 58px; height: 58px; }
  .stacked-lg .brand-name { font-size: 20px; letter-spacing: 3px; }
  .stacked-lg .brand-name span + span { margin-top: 3px; letter-spacing: 4.6px; }

  .inline .brand-dot { width: 42px; height: 42px; margin-right: 11px; }
  .inline .brand-name { font-size: 18px; letter-spacing: 2.6px; text-align: left; }
  .inline .brand-name span + span { margin-top: 3px; letter-spacing: 3.6px; }

  .holder { position: absolute; left: 21px; color: var(--brand-blue); }
  .holder-name { font-size: 15px; font-weight: 700; letter-spacing: 0.1px; }
  .holder-role { font-size: 10.5px; font-weight: 600; margin-top: 3px; margin-left: 1px; }

  .contact-list { position: absolute; list-style: none; color: var(--brand-blue); font-size: 11px; }
  .contact-list li { display: flex; align-items: flex-start; height: 13.7px; }
  .contact-list li.gap-top { margin-top: 5px; }
  .contact-list .icon { width: 11px; height: 11px; margin-right: 7px; margin-top: 1px; flex: none; color: var(--brand-green); }
  .contact-list .email { font-weight: 500; }

  .social { position: absolute; display: flex; gap: 7px; left: 217px; top: 143px; }
  .social-dot { width: 16px; height: 16px; border-radius: 50%; background: var(--brand-green); }
</style>
</head>
<body>

<svg width="0" height="0" style="position:absolute" aria-hidden="true">
  <defs>
    <symbol id="icon-mobile" viewBox="0 0 12 12"><rect x="3" y="0.7" width="6" height="10.6" rx="1" fill="none" stroke="currentColor" stroke-width="1.3"/><line x1="5" y1="9.6" x2="7" y2="9.6" stroke="currentColor" stroke-width="1"/></symbol>
    <symbol id="icon-mail" viewBox="0 0 12 12"><rect x="0.6" y="2.2" width="10.8" height="7.6" fill="currentColor"/><path d="M0.6 2.4 6 6.8 11.4 2.4" fill="none" stroke="#0c1522" stroke-width="1"/></symbol>
    <symbol id="icon-phone" viewBox="0 0 12 12"><path d="M2.4 1c.6-.4 1.2-.3 1.5.3l1 1.8c.3.5.1 1-.3 1.3l-.7.5c.5 1.3 1.5 2.3 2.8 2.8l.5-.7c.3-.4.8-.6 1.3-.3l1.8 1c.6.3.7.9.3 1.5l-.6.8C9.1 11.2 3.6 9.5 1 3.5c-.3-.8.1-1.6.6-2z" fill="currentColor"/></symbol>
    <symbol id="icon-globe" viewBox="0 0 12 12"><circle cx="6" cy="6" r="5.1" fill="none" stroke="currentColor" stroke-width="1.2"/><ellipse cx="6" cy="6" rx="2.2" ry="5.1" fill="none" stroke="currentColor" stroke-width="1"/><line x1="0.9" y1="6" x2="11.1" y2="6" stroke="currentColor" stroke-width="1"/></symbol>
    <symbol id="icon-pin" viewBox="0 0 12 12"><path d="M6 0.5a3.8 3.8 0 0 0-3.8 3.8C2.2 7.2 6 11.5 6 11.5s3.8-4.3 3.8-7.2A3.8 3.8 0 0 0 6 .5zm0 5.2a1.4 1.4 0 1 1 0-2.8 1.4 1.4 0 0 1 0 2.8z" fill="currentColor"/></symbol>
  </defs>
</svg>

<h1 class="sheet-title">BUSINESSCARD OPTIONS</h1>

<!-- Fronts -->
<section class="card card--a row-front">
  <div class="brand brand--stacked stacked-lg" style="left:0;right:0;top:45px;">
    <div class="brand-dot"></div>
    <div class="brand-name"><span>Lakemoor</span><span>Uniforms</span></div>
  </div>
</section>

<section class="card card--b row-front">
  <div class="brand brand--stacked stacked-lg" style="left:0;right:0;top:50px;">
    <div class="brand-dot"></div>
    <div class="brand-name"><span>Lakemoor</span><span>Uniforms</span></div>
  </div>
</section>

<section class="card card--c row-front">
  <div class="brand inline" style="left:72px;top:73px;">
    <div class="brand-dot"></div>
    <div class="brand-name"><span>Lakemoor</span><span>Uniforms</span></div>
  </div>
</section>

<!-- Backs -->
<section class="card card--a row-back">
  <div class="holder" style="top:56px;">
    <div class="holder-name">MARCUS WHITLOCK</div>
    <div class="holder-role">OWNER/ CEO</div>
  </div>
  <ul class="contact-list" style="left:21px;top:108px;">
    <li><svg class="icon"><use href="#icon-mobile"/></svg>(555) 014-2231</li>
    <li><svg class="icon"><use href="#icon-mobile"/></svg>(555) 018-4470</li>
    <li><svg class="icon"><use href="#icon-mail"/></svg>lakemoorshop@inbox.com</li>
  </ul>
  <div class="brand brand--stacked stacked-lg" style="left:183px;width:118px;top:22px;">
    <div class="brand-dot"></div>
    <div class="brand-name"><span>Lakemoor</span><span>Uniforms</span></div>
  </div>
</section>

<section class="card card--b row-back">
  <div class="holder" style="top:54px;left:29px;">
    <div class="holder-name">DANA WHITLOCK</div>
    <div class="holder-role">OWNER/ CEO</div>
  </div>
  <ul class="contact-list" style="left:29px;top:106px;">
    <li><svg class="icon"><use href="#icon-mobile"/></svg>(555) 014-6620</li>
    <li><svg class="icon"><use href="#icon-mobile"/></svg>(555) 018-4470</li>
    <li class="email"><svg class="icon"><use href="#icon-mail"/></svg>lakemoorshop@inbox.com</li>
  </ul>
  <div class="brand brand--stacked stacked-lg" style="left:187px;width:118px;top:20px;">
    <div class="brand-dot"></div>
    <div class="brand-name"><span>Lakemoor</span><span>Uniforms</span></div>
  </div>
</section>

<section class="card card--c row-back">
  <div class="brand inline" style="left:19px;top:25px;">
    <div class="brand-dot"></div>
    <div class="brand-name"><span>Lakemoor</span><span>Uniforms</span></div>
  </div>
  <ul class="contact-list" style="left:19px;top:86px;">
    <li><svg class="icon"><use href="#icon-phone"/></svg>(555) 017-3390</li>
    <li><svg class="icon"><use href="#icon-mail"/></svg>hello@lakemooruniforms.com</li>
    <li><svg class="icon"><use href="#icon-globe"/></svg>www.lakemooruniforms.com</li>
    <li class="gap-top"><svg class="icon"><use href="#icon-pin"/></svg>48 Ridgeview Commons</li>
    <li><span style="width:18px;flex:none"></span>Pine Hollow, NC 28015</li>
  </ul>
  <div class="social" aria-label="Social media links">
    <span class="social-dot"></span><span class="social-dot"></span><span class="social-dot"></span><span class="social-dot"></span>
  </div>
</section>

</body>
</html>
```